need a graphic redesign of kestrowcare.com

Need a graphic redesign of kestrowcare.com. We need to make it more user friendly as well as SEO friendly. All information is there. We have lot of stock photos (done our own photoshoot).

We want this website to be redesigned from scratch. Please avoid using pre made templates. Recommend people who really understand design to approach this project.

Target population is Non resident Indians who live outside India but their families are still in India and need for health care.

Logos and pictures are on the website but we can provide raw images.

Target Market(s)

Industry/Entity Type

Healthcare

Number of Pages Required

5+ page

Font styles to use
Serif
Sans Serif

Requirements
Must have
• Good design, and use of minimal text. Design need to be responsive (we know it is a later process in coding- but mobile devices need to be kept in mind)
Nice to have
• We need a original design.
Should not have
• prebuilt or copied templates

```html
<!DOCTYPE html>
<html lang="en">
<head>
<meta charset="utf-8">
<title>Partner With Us – Kestrow Care</title>
<link rel="stylesheet" href="https://fonts.googleapis.com/css2?family=Oswald:wght@300;400&family=Roboto+Condensed:wght@400;700&display=swap">
<style>
:root{
  --teal:#4f8f80;
  --teal-dark:#2f5f55;
  --teal-text:#3f8a7a;
  --mint:#a9d5c8;
  --mint-pale:#d6ece5;
  --ink:#2d2d2d;
  --white:#ffffff;
  --field:#ffffff;
  --field-line:#5c8f84;
}
*{box-sizing:border-box;margin:0;padding:0}
html,body{width:826px;height:1200px;overflow:hidden;background:var(--white)}
body{position:relative;font-family:"Roboto Condensed",Arial,sans-serif;color:var(--ink)}
.abs{position:absolute}

.hero{left:0;top:0;width:610px;height:330px;background:linear-gradient(100deg,#ece7e2 0%,#d9c2aa 30%,#f2e7d8 55%,#c9cfcc 100%)}
.logo-box{left:22px;top:0;width:110px;height:76px;background:var(--white);display:flex;flex-direction:column;align-items:center;justify-content:center;gap:4px}
.logo-dot{width:16px;height:16px;border-radius:50%;background:#e8772e}
.logo-name{font-family:"Roboto Condensed",sans-serif;font-size:14px;color:var(--teal-text)}

.nav{left:132px;top:14px;width:478px;height:30px;background:var(--teal);display:flex;align-items:center;justify-content:space-around;padding:0 8px}
.nav a{font-family:"Oswald",sans-serif;font-size:11px;color:var(--white);text-decoration:none;letter-spacing:.3px}
.nav a.active{font-weight:400;color:#e9f6f2}

.login{left:627px;top:0;width:135px;height:106px;background:var(--mint);padding:24px 10px 0;text-align:center}
.btn-outline{display:block;margin:0 auto;width:112px;height:22px;border:1px solid var(--teal-dark);border-radius:12px;background:var(--mint-pale);font-family:"Oswald",sans-serif;font-size:11px;color:var(--teal-dark);line-height:20px}
.login p{font-size:7px;color:var(--teal-dark);margin:8px 0 8px;line-height:1.2}

.request{left:610px;top:283px;width:155px;height:393px;background:var(--mint);padding:12px 12px}
.request h3{font-family:"Oswald",sans-serif;font-weight:400;font-size:17px;line-height:1.1;color:var(--teal-dark);text-align:center;margin-bottom:14px}
.request label{display:block;font-size:9px;color:var(--ink);margin-bottom:3px}
.request .fld{height:20px;background:var(--field);border:1px solid var(--field-line);border-radius:10px;margin-bottom:13px}
.request .area{height:72px;border-radius:6px}
.request .send{margin:18px auto 0;width:76px;height:20px;border-radius:10px;background:var(--teal);color:var(--white);font-family:"Oswald",sans-serif;font-size:10px;text-align:center;line-height:20px}

.intro{left:124px;top:344px;width:460px;font-size:15px;line-height:1.55;color:var(--teal-text)}
.title{left:0;top:436px;width:610px;text-align:center;font-family:"Oswald",sans-serif;font-weight:300;font-size:30px;color:var(--teal-text)}

.form{left:0;top:503px;width:610px}
.row{display:flex;align-items:center;height:40px}
.row label{width:242px;text-align:right;font-size:10px;padding-right:10px;color:var(--ink)}
.row .fld{width:242px;height:20px;border:1px solid var(--field-line);border-radius:10px;background:var(--field)}
.submit{left:253px;top:806px;width:130px;height:24px;border-radius:12px;background:var(--teal);color:var(--white);font-family:"Oswald",sans-serif;font-size:10px;text-align:center;line-height:24px}

.footer{left:0;top:900px;width:826px;height:222px;background:var(--teal);color:var(--white)}
.touch{left:33px;top:30px;font-family:"Oswald",sans-serif;font-weight:300;font-size:30px}
.contact{left:33px;display:flex;align-items:center;gap:10px;font-size:11px}
.flag{width:44px;height:44px;border-radius:50%;background:#f0f0f0}
.office h4{font-size:12px;font-weight:700;margin-bottom:6px}
.office p{font-size:9.5px;line-height:1.55}

.social{left:0;top:1122px;width:826px;height:78px;background:var(--teal-dark);display:flex;justify-content:center;align-items:center;gap:10px}
.social span{width:30px;height:30px;border:1px solid rgba(255,255,255,.7)}
</style>
</head>
<body>

<div class="abs hero" role="img" aria-label="Photo of a smiling senior couple embracing"></div>

<div class="abs logo-box"><span class="logo-dot"></span><span class="logo-name">Kestrow Care</span></div>

<nav class="abs nav">
  <a href="#">HOME</a><a href="#">ABOUT US</a><a href="#">SERVICES</a><a href="#">OUR NETWORK</a><a href="#" class="active">PARTNER WITH US</a><a href="#">CONTACT US</a>
</nav>

<aside class="abs login">
  <span class="btn-outline">MEMBER LOGIN</span>
  <p>Get a login to access the full range of services</p>
  <span class="btn-outline">SIGN UP</span>
</aside>

<aside class="abs request">
  <h3>REQUEST MORE<br>INFORMATION</h3>
  <label>Name</label><div class="fld"></div>
  <label>E-mail</label><div class="fld"></div>
  <label>Phone Number</label><div class="fld"></div>
  <label>Enquiry</label><div class="fld area"></div>
  <div class="send">SEND</div>
</aside>

<p class="abs intro">Please fill out the form below and we will get in touch with you as quickly as we can.</p>
<h1 class="abs title">PARTNER WITH US</h1>

<form class="abs form">
  <div class="row"><label>Name of the Service Provider</label><span class="fld"></span></div>
  <div class="row"><label>Contact Number</label><span class="fld"></span></div>
  <div class="row"><label>Alternative Contact Number</label><span class="fld"></span></div>
  <div class="row"><label>Email</label><span class="fld"></span></div>
  <div class="row"><label>Website</label><span class="fld"></span></div>
  <div class="row"><label>City/State</label><span class="fld"></span></div>
  <div class="row"><label>Service</label><span class="fld"></span></div>
</form>
<div class="abs submit">SUBMIT</div>

<footer class="abs footer">
  <div class="abs touch">Get in touch</div>
  <div class="abs contact" style="top:88px">
    <svg width="16" height="16" viewBox="0 0 16 16"><circle cx="8" cy="8" r="8" fill="#fff"/><path d="M5 4.5l1.6-.4 1 2.2-1 .8a6 6 0 0 0 2.3 2.3l.8-1 2.2 1-.4 1.6c-3.6.4-6.9-2.9-6.5-6.5z" fill="#4f8f80"/></svg>
    +91 9210 555 0134
  </div>
  <div class="abs contact" style="top:116px">
    <svg width="16" height="16" viewBox="0 0 16 16"><circle cx="8" cy="8" r="8" fill="#fff"/><rect x="4" y="5" width="8" height="6" fill="none" stroke="#4f8f80"/><path d="M4 5l4 3 4-3" fill="none" stroke="#4f8f80"/></svg>
    info@kestrowcare.com
  </div>

  <span class="abs flag" style="left:242px;top:36px"></span>
  <div class="abs office" style="left:302px;top:38px">
    <h4>Registered Office:</h4>
    <p>Level 4, Arlen Court,<br>Ridge Park Road<br>Gurgaon- 122018<br>Haryana, India</p>
  </div>
  <div class="abs office" style="left:454px;top:38px">
    <h4>Corporate Office:</h4>
    <p>812 Lotus Tower,<br>Civic Centre<br>Vikas Nagar- 110071<br>New Delhi, India<br>Landline No: +91 2555-0142<br>Fax No: +91 2555-0198</p>
  </div>
  <span class="abs flag" style="left:606px;top:36px"></span>
  <div class="abs office" style="left:671px;top:38px">
    <h4>Our US Office:</h4>
    <p>4120 W Canyon Road,<br>Suite 208,<br>Mesa, AZ 85201<br>United States</p>
  </div>
</footer>

<div class="abs social">
  <span></span><span></span><span></span><span></span><span></span><span></span><span></span><span></span><span></span><span></span>
</div>

</body>
</html>
```